Norvale - Business Card Design

Design a modern masculine business card for our business

Target Market(s)

Private Market

Industry/Entity Type

Construction

Contact Information for Business Card

Company Name - Name of Person - Address - email address - contact number

Font styles to use
Serif
Sans Serif

Colors
0094D4
00A9DD
6FCCEA
C7EBF8
E9F6FB
00AB8E
00BBA5
67D7C9
C6EFE9
E9F9F6
F0912C
F2A743
F7CA91
FBE8D2
FDF5EE

Requirements
Must have
• Use company logo provided
Nice to have
• Company Logo

```html
<!DOCTYPE html>
<html lang="en">
<head>
<meta charset="UTF-8">
<title>Norvale – Business Card</title>
<link rel="stylesheet" href="https://fonts.googleapis.com/css2?family=Poppins:wght@400;500;800&display=swap">
<style>
  :root {
    --page-bg: #2a2a2a;
    --card-bg: #0d0d0d;
    --accent: #f0742c;
    --text-light: #d6d6d6;
    --text-muted: #b0b0b0;
    --rule: #555555;
    --silver: #c9c9c9;
  }
  * { margin: 0; padding: 0; box-sizing: border-box; }
  html, body {
    width: 1200px; height: 900px; overflow: hidden;
    background: var(--page-bg);
    font-family: "Poppins", sans-serif;
  }
  .sheet {
    width: 1200px; height: 900px;
    display: flex; flex-direction: column;
    align-items: center; justify-content: center; gap: 56px;
  }
  .card {
    width: 640px; height: 366px;
    background: var(--card-bg);
    border-radius: 22px;
    position: relative;
    box-shadow: 0 14px 36px rgba(0,0,0,0.55);
    overflow: hidden;
  }
  .brand {
    display: flex; align-items: center; gap: 10px;
    font-weight: 800; letter-spacing: 1px; text-transform: uppercase;
    white-space: nowrap;
  }
  .brand-square { width: 16px; height: 16px; background: var(--accent); flex: none; }
  .card-front .brand {
    position: absolute; left: 40px; top: 178px;
    font-size: 44px; color: #ffffff;
  }
  .divider {
    position: absolute; left: 318px; top: 110px;
    width: 1px; height: 190px; background: var(--rule);
  }
  .details {
    position: absolute; left: 346px; top: 92px;
    color: var(--text-light);
  }
  .person-name {
    color: var(--accent); font-size: 21px; font-weight: 500;
    text-transform: uppercase; line-height: 1.1;
  }
  .person-role { color: var(--text-muted); font-size: 15px; margin-bottom: 14px; }
  .contact-list { list-style: none; }
  .contact-list li {
    display: flex; align-items: center; gap: 9px;
    font-size: 15px; line-height: 1.55;
  }
  .contact-list svg { width: 15px; height: 15px; fill: var(--accent); flex: none; }
  .address { margin-top: 16px; font-size: 15px; line-height: 1.35; }
  .card-back { display: flex; align-items: center; justify-content: center; }
  .card-back .brand { font-size: 58px; color: var(--silver); }
  .card-back .brand-square { background: var(--silver); width: 20px; height: 20px; }
</style>
</head>
<body>
<main class="sheet">
  <section class="card card-front">
    <div class="brand"><span class="brand-square"></span>Norvale</div>
    <div class="divider"></div>
    <div class="details">
      <p class="person-name">Marcus Hale</p>
      <p class="person-role">Managing Director</p>
      <ul class="contact-list">
        <li><svg viewBox="0 0 24 24"><path d="M6.6 10.8a15.1 15.1 0 0 0 6.6 6.6l2.2-2.2a1 1 0 0 1 1-.25 11.4 11.4 0 0 0 3.6.57 1 1 0 0 1 1 1V20a1 1 0 0 1-1 1A17 17 0 0 1 3 4a1 1 0 0 1 1-1h3.5a1 1 0 0 1 1 1c0 1.25.2 2.45.57 3.57a1 1 0 0 1-.25 1z"/></svg>044-555 210 347</li>
        <li><svg viewBox="0 0 24 24"><path d="M2 5h20v14H2z M2 5l10 8 10-8" /></svg>info@norvalebuild.com</li>
        <li><svg viewBox="0 0 24 24"><path d="M12 2a10 10 0 1 0 0 20 10 10 0 0 0 0-20zm0 2c1.2 0 2.6 2.3 3 6H9c.4-3.7 1.8-6 3-6zm-7.7 6A8 8 0 0 1 7.6 5 13 13 0 0 0 7 10zm0 4H7c.1 1.9.5 3.6 1.1 5a8 8 0 0 1-3.8-5zM9 14h6c-.4 3.7-1.8 6-3 6s-2.6-2.3-3-6zm8 0h2.7a8 8 0 0 1-3.8 5c.6-1.4 1-3.1 1.1-5zm0-4c-.1-1.9-.5-3.6-1.1-5a8 8 0 0 1 3.8 5z"/></svg>www.norvalebuild.com</li>
      </ul>
      <p class="address">87, Quarry Road Street<br>45219, Northland</p>
    </div>
  </section>
  <section class="card card-back">
    <div class="brand"><span class="brand-square"></span>Norvale</div>
  </section>
</main>
</body>
</html>
```